Solar Advertising Flier to generate Biz

I need a advertisement that generates business to be used in a mailer for marketing purposes.

Im attaching a file that is a an idea of advertisement.
I do not want the "ZVN" specific information on it.
I want the background solar panels.
Same information as the ad.
And I've attached my Logo - I want the color scheme to match this.

Thank you

Target Market(s)

Middle to Upper Class Home Owners

Industry/Entity Type

Solar Energy

Requirements
Must have
• A call to action
• A professional look
Nice to have
• A family
• Great looking solar panels
Should not have
• Cartoons

```html
<!DOCTYPE html>
<html lang="en">
<head>
<meta charset="utf-8">
<title>Go Solar Mailer</title>
<link href="https://fonts.googleapis.com/css2?family=Montserrat:wght@600;700;800&family=Questrial&display=swap" rel="stylesheet">
<style>
:root{
  --blue:#1b8fd4;
  --green:#9ccb3b;
  --green-light:#d4e52a;
  --orange:#ef7d1a;
  --ink:#1d1d1d;
  --white:#ffffff;
  --sky:#b9cfe0;
  --grass:#7fae3a;
}
*{margin:0;padding:0;box-sizing:border-box}
html,body{width:940px;height:1200px;overflow:hidden;background:#6e6e6e}
.flyer{position:relative;width:940px;height:1200px;background:var(--white);overflow:hidden;font-family:"Questrial",sans-serif;color:var(--ink)}
.hero-photo{position:absolute;left:0;top:0;width:940px;height:462px;
  background:linear-gradient(180deg,#dfe8ef 0%,var(--sky) 30%,#6f7f95 52%,#4f5d74 66%,#8db150 78%,var(--grass) 100%)}
.headline{position:absolute;top:62px;left:0;width:940px;text-align:center;font-family:"Montserrat",sans-serif;font-weight:800;font-size:108px;letter-spacing:2px;color:var(--blue);text-shadow:4px 4px 0 rgba(0,0,0,.35);line-height:1}
.subhead{position:absolute;top:166px;left:0;width:940px;text-align:center;font-family:"Montserrat",sans-serif;font-weight:700;font-size:23px;color:var(--white);text-shadow:1px 1px 3px rgba(0,0,0,.5)}
.white-wave{position:absolute;left:0;top:420px}
.brand-dot{position:absolute;left:410px;top:392px;width:114px;height:114px;border-radius:50%;border:9px solid var(--green);background:var(--white)}
.brand-name{position:absolute;left:300px;top:544px;width:334px;text-align:center;font-family:"Montserrat",sans-serif;font-weight:600;color:var(--blue);line-height:1}
.brand-name .line-1{display:block;font-size:31px}
.brand-name .line-2{display:block;font-size:19px;margin-top:8px;letter-spacing:3px}
.offer-circle{position:absolute;left:-191px;top:469px;width:513px;height:513px;border-radius:50%;border:5px solid var(--blue);
  background:radial-gradient(circle at 60% 35%,var(--green-light) 0%,#b4d62d 45%,var(--green) 100%)}
.offer-lead{position:absolute;left:75px;top:596px;font-family:"Montserrat",sans-serif;font-weight:600;font-size:21px;line-height:1.25;color:#2a2a2a}
.offer-amount{position:absolute;left:72px;top:648px;font-family:"Montserrat",sans-serif;font-weight:800;font-size:80px;line-height:1;color:var(--blue);text-shadow:3px 3px 0 rgba(0,0,0,.3);letter-spacing:-2px}
.offer-amount sup{font-size:38px;vertical-align:top;position:relative;top:4px}
.offer-tag{position:absolute;left:73px;top:731px;width:247px;height:34px;background:var(--blue);color:var(--white);font-family:"Montserrat",sans-serif;font-weight:600;font-size:24px;line-height:34px;text-align:center}
.offer-terms{position:absolute;left:75px;top:774px;width:190px;font-size:13px;line-height:1.33;color:#222}
.benefits-bar{position:absolute;left:310px;top:631px;width:630px;height:46px;background:var(--blue);color:var(--white);font-family:"Montserrat",sans-serif;font-weight:600;font-size:34px;line-height:46px;padding-left:67px}
.benefits{position:absolute;left:377px;top:686px;width:540px;list-style:none;font-size:19px;line-height:24.5px}
.benefits li{position:relative;padding-left:16px}
.benefits li::before{content:"•";position:absolute;left:0}
.benefits b,.how-text b{font-family:"Montserrat",sans-serif;font-weight:700;font-size:17px}
.how-title{position:absolute;left:377px;top:832px;font-family:"Montserrat",sans-serif;font-weight:600;font-size:28px;line-height:34px;color:var(--blue)}
.how-text{position:absolute;left:377px;top:870px;width:520px;font-size:19px;line-height:24.5px}
.footer-band{position:absolute;left:0;top:1014px;width:940px;height:186px;background:var(--green)}
.footer-logo{position:absolute;left:0;top:1004px;width:360px;height:78px;background:var(--white);display:flex;align-items:center;justify-content:center;gap:10px}
.footer-logo .mark{width:22px;height:22px;border-radius:50%;background:var(--orange)}
.footer-logo .name{font-family:"Montserrat",sans-serif;font-weight:800;font-size:28px;color:var(--orange);white-space:nowrap}
.cta-line{position:absolute;left:380px;top:1026px;font-family:"Montserrat",sans-serif;font-weight:600;font-size:17px;color:#1d1d1d}
.cta-phone{position:absolute;left:378px;top:1046px;font-family:"Montserrat",sans-serif;font-weight:800;font-size:48px;line-height:54px;color:var(--white)}
.address{position:absolute;left:0;top:1108px;width:940px;text-align:center;font-family:"Montserrat",sans-serif;font-weight:600;font-size:17px;color:#1d1d1d}
</style>
</head>
<body>
<div class="flyer">
  <div class="hero-photo" role="img" aria-label="Rows of ground-mounted solar panels on a green field under a cloudy blue sky, framed by trees"></div>
  <svg class="white-wave" width="940" height="60" viewBox="0 0 940 60" aria-hidden="true">
    <path d="M0 26 Q470 8 940 -4 L940 60 L0 60 Z" fill="#ffffff"/>
  </svg>
  <h1 class="headline">GO SOLAR</h1>
  <p class="subhead">Get Grandfathered Before the New ZVN Deadline</p>

  <div class="brand-dot"></div>
  <div class="brand-name"><span class="line-1">BRIGHT HORIZON</span><span class="line-2">ENERGY</span></div>

  <div class="offer-circle"></div>
  <p class="offer-lead">Call Today<br>and Receive a</p>
  <p class="offer-amount"><sup>$</sup>500</p>
  <div class="offer-tag">CASH REBATE</div>
  <p class="offer-terms">Limited time offer. Ad must be present at time of purchase. Call for details. Not valid with any other offer or on previous purchases.</p>

  <div class="benefits-bar">We Make It Easy</div>
  <ul class="benefits">
    <li><b>$0 Down</b>, No upfront cost.</li>
    <li><b>Save up to 90%</b> off your utility bill.</li>
    <li>Protect against inflation &amp; energy costs increases<br>from your Utility Company.</li>
    <li>Provide clean, reliable energy for your family<br><b>powered by the sun.</b></li>
  </ul>
  <h2 class="how-title">How it works...</h2>
  <p class="how-text">Your solar system allows you to <b>generate your own</b><br><b>clean power</b> and COSTS LESS than your current<br>utility company. Simply pay by the month,<br>like you do now...but at a LOWER rate and<br><b>START SAVING IMMEDIATELY.</b></p>

  <div class="footer-band"></div>
  <div class="footer-logo"><span class="mark"></span><span class="name">HELIOPATH SOLAR</span></div>
  <p class="cta-line">Call Today For A No Obligation Consultation</p>
  <p class="cta-phone">555-014-2287</p>
  <p class="address">1840 W Cactus Bloom Rd B-220 • Glendale AZ 85301 • www.HelioPathSolar.com</p>
</div>
</body>
</html>
```